Oil & Gas Service Brochure

We need to create a brochure that highlights the benefits of one of our services to oil and gas wells. We have a word document that includes a summary of the service and its problem solving benefits as well as some photos. The task will be to create a brochure using this information and our company logo and color schemes. Additionally, copy editing and proofing is preferred.

Target Market(s)

Oil & Gas Well Operators

```html
<!DOCTYPE html>
<html lang="en">
<head>
<meta charset="utf-8">
<title>Well Service Brochure – Benefits &amp; Work Summary</title>
<link href="https://fonts.googleapis.com/css2?family=Bebas+Neue&family=Montserrat:wght@700;800&family=Work+Sans:wght@400;500;700&display=swap" rel="stylesheet">
<style>
  :root{
    --navy:#0a4d80;
    --navy-deep:#0b1f4f;
    --orange:#f7941d;
    --panel:#eeeeee;
    --photo-a:#c3dbe1;
    --photo-b:#d4e7eb;
    --box-fill:#f6f8f9;
    --link-green:#6a9e74;
    --link-navy:#2c5c86;
    --text:#0a4d80;
  }
  *{margin:0;padding:0;box-sizing:border-box}
  html,body{width:927px;height:1200px;overflow:hidden;background:#fff}
  .page{position:relative;width:927px;height:1200px;overflow:hidden;font-family:"Work Sans",Arial,sans-serif;color:var(--text)}

  .benefits{position:absolute;left:0;top:0;width:927px;height:463px;background:var(--panel)}
  .benefits__title{position:absolute;left:0;right:0;top:84px;text-align:center;font-family:"Bebas Neue","Oswald",sans-serif;font-size:62px;letter-spacing:1.5px;line-height:1;color:var(--navy)}
  .benefit{position:absolute;width:330px}
  .benefit__tick{position:absolute;left:-64px;top:0;width:47px;height:42px}
  .benefit__text{font-size:14.3px;line-height:18.1px;letter-spacing:.1px}
  .benefit__text strong{font-weight:700}
  .benefit--1{left:133px;top:182px}
  .benefit--2{left:551px;top:182px}
  .benefit--3{left:133px;top:328px}
  .benefit--4{left:549px;top:327px}

  .summary{position:absolute;left:0;top:463px;width:927px;height:737px}
  .summary__photo{position:absolute;inset:0;background:linear-gradient(160deg,var(--photo-b),var(--photo-a) 60%,#b9d3da)}
  .summary__waves{position:absolute;left:0;top:0;width:927px;height:1200px;z-index:1}
  .summary__title{position:absolute;left:76px;top:141px;font-family:"Bebas Neue","Oswald",sans-serif;font-size:44px;letter-spacing:1px;line-height:1;color:var(--navy);z-index:2}
  .summary__intro{position:absolute;left:81px;top:200px;width:350px;font-size:24px;line-height:29px;color:var(--navy);z-index:2}

  .steps{position:absolute;left:0;top:0;z-index:3}
  .steps__link{position:absolute;left:520px;top:570px;width:9px;height:480px;background:linear-gradient(var(--link-green) 0 48%,var(--link-navy) 52% 100%)}
  .step{position:absolute;left:471px;width:404px;background:var(--box-fill);border:4.5px solid var(--navy);display:flex;align-items:center;box-shadow:2px 3px 6px rgba(0,0,0,.12)}
  .step__num{flex:0 0 auto;width:86px;padding-left:22px;font-family:"Montserrat",Arial,sans-serif;font-weight:800;font-size:35px;color:var(--navy)}
  .step__text{font-size:12.6px;line-height:16.4px;letter-spacing:.15px;padding-right:10px}
  .step--1{top:517px;height:55px}
  .step--2{top:587px;height:75px}
  .step--3{top:677px;height:113px}
  .step--4{top:806px;height:127px}
  .step--5{top:952px;height:59px}
  .step--6{top:1030px;height:58px}
</style>
</head>
<body>
<div class="page">

  <section class="benefits">
    <h1 class="benefits__title">THE MAIN BENEFITS ARE:</h1>

    <div class="benefit benefit--1">
      <svg class="benefit__tick" viewBox="0 0 47 42" aria-hidden="true"><rect x="2" y="4" width="36" height="35" rx="5" fill="none" stroke="#f7941d" stroke-width="4"/><path d="M10 19 L19 28 L44 4" fill="none" stroke="#f7941d" stroke-width="6" stroke-linecap="round" stroke-linejoin="round"/></svg>
      <p class="benefit__text">For a small investment, we can provide helpful information to determine if the well needs to be worked over or not. I.e., if we perform this service and nothing changes, you know you have wellbore issues NOT production tubing issues.</p>
    </div>

    <div class="benefit benefit--2">
      <svg class="benefit__tick" viewBox="0 0 47 42" aria-hidden="true"><rect x="2" y="4" width="36" height="35" rx="5" fill="none" stroke="#f7941d" stroke-width="4"/><path d="M10 19 L19 28 L44 4" fill="none" stroke="#f7941d" stroke-width="6" stroke-linecap="round" stroke-linejoin="round"/></svg>
      <p class="benefit__text">When the service is successful, the data has shown <strong>an increase of 100%-600% in production</strong>! For example, wells that were making 2-3BBL/day before we performed this service are now producing 50-70BBL/day!</p>
    </div>

    <div class="benefit benefit--3">
      <svg class="benefit__tick" viewBox="0 0 47 42" aria-hidden="true"><rect x="2" y="4" width="36" height="35" rx="5" fill="none" stroke="#f7941d" stroke-width="4"/><path d="M10 19 L19 28 L44 4" fill="none" stroke="#f7941d" stroke-width="6" stroke-linecap="round" stroke-linejoin="round"/></svg>
      <p class="benefit__text">This service is “greener” than a traditional workover by producing far less emissions. There is no need to kill the well or to flare any gas.</p>
    </div>

    <div class="benefit benefit--4">
      <svg class="benefit__tick" viewBox="0 0 47 42" aria-hidden="true"><rect x="2" y="4" width="36" height="35" rx="5" fill="none" stroke="#f7941d" stroke-width="4"/><path d="M10 19 L19 28 L44 4" fill="none" stroke="#f7941d" stroke-width="6" stroke-linecap="round" stroke-linejoin="round"/></svg>
      <p class="benefit__text">This service is cost effective enough that in most cases, the “free” increased production will pay for this service in 24-48 hours.</p>
    </div>
  </section>

  <section class="summary">
    <div class="summary__photo" role="img" aria-label="Faded blue-tinted photo of a drilling rig at a well site"></div>
    <h2 class="summary__title">WORK SUMMARY:</h2>
    <p class="summary__intro">This service can be done in a few hours if no unexpected well conditions are encountered. A typical job would look something like this.</p>
  </section>

  <svg class="summary__waves" viewBox="0 0 1688 2184" preserveAspectRatio="none" aria-hidden="true">
    <defs>
      <linearGradient id="waveGreen" x1="0" y1="0" x2="1" y2="0">
        <stop offset="0" stop-color="#5ee38a"/>
        <stop offset=".5" stop-color="#3aa590"/>
        <stop offset="1" stop-color="#7dff7a"/>
      </linearGradient>
      <linearGradient id="waveTeal" x1="0" y1="0" x2="1" y2="0">
        <stop offset="0" stop-color="#1c6f9a"/>
        <stop offset=".45" stop-color="#3ea38e"/>
        <stop offset="1" stop-color="#6be07e"/>
      </linearGradient>
      <linearGradient id="waveBlue" x1="0" y1="1" x2="1" y2="0">
        <stop offset="0" stop-color="#0b2c78"/>
        <stop offset="1" stop-color="#0a4fa8"/>
      </linearGradient>
    </defs>
    <path d="M0 1775 C300 1755 600 1820 900 1880 C1200 1940 1450 1880 1688 1680 L1688 2184 L0 2184 Z" fill="url(#waveGreen)"/>
    <path d="M0 1895 C400 1880 750 1960 1050 1985 C1300 2005 1500 1940 1688 1800 L1688 2184 L0 2184 Z" fill="url(#waveTeal)"/>
    <path d="M0 2184 L0 2130 C250 2065 600 2085 900 2100 C1250 2110 1500 2010 1688 1880 L1688 2184 Z" fill="url(#waveBlue)"/>
    <path d="M450 2184 C700 2100 1050 2130 1300 2090 C1480 2060 1600 2000 1688 1950 L1688 2184 Z" fill="#071a4a"/>
    <path d="M0 2184 L0 2150 C150 2110 350 2120 520 2150 L560 2184 Z" fill="#06143c"/>
  </svg>

  <div class="steps">
    <div class="steps__link"></div>
    <div class="step step--1"><span class="step__num">01</span><p class="step__text">MIRU Slickline, RIH and pull plunger noting tight spots</p></div>
    <div class="step step--2"><span class="step__num">02</span><p class="step__text">RIH and pull BSSV-note depth of nipple so we can correlate to tubing tally and wellbore diagram</p></div>
    <div class="step step--3"><span class="step__num">03</span><p class="step__text">RIH with “dummy run” (Ridgeway Jars, Weight bars, Blind Box and Temperature Probe) drift through Profile Nipples to determine Perf Sub depth, establish bottom hole temperature and to locate fluid level.</p></div>
    <div class="step step--4"><span class="step__num">04</span><p class="step__text">Once depths, fluid level and temperature have been confirmed and we know we are deep enough to get into the Perf Sub, RIHW SureStrike System® and either perforate new holes using a RTG (Retrievable Tubing Gun) or remove scale utilizing our ClearScale Charge®.</p></div>
    <div class="step step--5"><span class="step__num">05</span><p class="step__text">Free flow well to determine if new or more communication has been established.</p></div>
    <div class="step step--6"><span class="step__num">06</span><p class="step__text">RIHW broach to production nipple. Reset production tools and turn well back to the client</p></div>
  </div>

</div>
</body>
</html>
```